Corporate consulting business needs a business card

I want a professional business card.... surprise me

Target Market(s)

Corprorate and Not for Profit firms and organisations

Industry/Entity Type

Consulting

Contact Information for Business Card

Logo
Corporate Consulting Services
Clear Plans, Sound Budgets, Lasting Results
Tobin Averley
Director
0427 31 64 92 (Larger)
tobin@ta-advisory.com.au
www.ta-advisory.com.au
include little icons beside the contact info:

- Envelope = email
- Phone = phone
- Globe = website

Font styles to use
Serif
Sans Serif

Requirements
Must have
• Professional and clean
Nice to have
• you tell me

```html
<!DOCTYPE html>
<html lang="en">
<head>
<meta charset="utf-8">
<title>TA Advisory Services – Business Card</title>
<link rel="stylesheet" href="https://fonts.googleapis.com/css2?family=EB+Garamond:ital,wght@0,400;0,600;0,700;1,400&display=swap">
<style>
  :root {
    --bg-light: #d9d9d9;
    --bg-dark: #8a8a8a;
    --card: #ffffff;
    --ink: #111111;
    --brown: #5a2e1a;
    --brown-soft: #7a4a30;
    --serif: "EB Garamond", Georgia, serif;
  }
  * { box-sizing: border-box; margin: 0; padding: 0; }
  html, body { width: 1200px; height: 960px; overflow: hidden; }
  body {
    background: radial-gradient(ellipse at 50% 40%, var(--bg-light) 0%, #b5b5b5 55%, var(--bg-dark) 100%);
    font-family: var(--serif);
    color: var(--ink);
    position: relative;
  }
  .card {
    position: absolute;
    top: 326px;
    width: 540px;
    height: 309px;
    background: var(--card);
    box-shadow: 0 10px 30px rgba(0,0,0,.25);
    overflow: hidden;
  }
  .card--front { left: 40px; }
  .card--back { left: 620px; }

  /* Front */
  .front-mark {
    position: absolute;
    inset: 0;
    display: flex; align-items: center; justify-content: center; gap: 16px;
  }
  .front-mark__circle {
    width: 40px; height: 40px;
    border: 4px solid var(--brown);
    border-radius: 50%;
    flex: none;
  }
  .front-mark__name {
    font-weight: 700;
    font-size: 29px;
    letter-spacing: .04em;
    text-transform: uppercase;
    color: var(--ink);
    white-space: nowrap;
  }

  /* Back */
  .holder { position: absolute; left: 40px; top: 34px; }
  .holder__name { font-weight: 700; font-size: 19px; }
  .holder__role { font-size: 15px; color: var(--brown-soft); margin-top: -2px; }

  .brand {
    position: absolute; right: 34px; top: 100px;
    text-align: right;
  }
  .brand__company {
    display: flex; justify-content: flex-end; align-items: center; gap: 10px;
    font-weight: 700; font-size: 17px; color: var(--brown);
  }
  .brand__circle {
    width: 18px; height: 18px;
    border: 2px solid var(--brown);
    border-radius: 50%;
    flex: none;
  }
  .brand__line { font-weight: 700; font-size: 15px; margin-top: 4px; }
  .brand__tagline { font-style: italic; font-size: 13.5px; }

  .contacts {
    position: absolute; right: 34px; bottom: 30px;
    list-style: none;
  }
  .contacts li {
    display: flex; justify-content: flex-end; align-items: center; gap: 10px;
    font-size: 14px; line-height: 1.45;
  }
  .contacts .contact--phone { font-weight: 700; font-size: 20px; }
  .contacts svg { width: 13px; height: 13px; flex: none; }
  .icon { fill: none; stroke: var(--brown); stroke-width: 1.6; stroke-linecap: round; stroke-linejoin: round; }
</style>
</head>
<body>

  <section class="card card--front" aria-label="Business card front">
    <div class="front-mark">
      <div class="front-mark__circle"></div>
      <div class="front-mark__name">TA Advisory Services</div>
    </div>
  </section>

  <section class="card card--back" aria-label="Business card back">
    <div class="holder">
      <div class="holder__name">Tobin Averley</div>
      <div class="holder__role">Director</div>
    </div>

    <div class="brand">
      <div class="brand__company"><span class="brand__circle"></span>TA Advisory Services</div>
      <div class="brand__line">Corporate Consulting Services</div>
      <div class="brand__tagline">Clear Plans, Sound Budgets, Lasting Results</div>
    </div>

    <ul class="contacts">
      <li class="contact--phone">0427 31 64 92
        <svg viewBox="0 0 16 16" aria-hidden="true"><path class="icon" d="M4 1.5l2.5 3-1.5 1.8c.8 1.8 2.2 3.2 4 4l1.8-1.5 3 2.5-1.6 2.2C7.5 13.3 2.7 8.5 1.8 3.1z"/></svg>
      </li>
      <li>tobin@ta-advisory.com.au
        <svg viewBox="0 0 16 16" aria-hidden="true"><rect class="icon" x="1.5" y="3.5" width="13" height="9" rx="1"/><polyline class="icon" points="1.5,4 8,9 14.5,4"/></svg>
      </li>
      <li>www.ta-advisory.com.au
        <svg viewBox="0 0 16 16" aria-hidden="true"><circle class="icon" cx="8" cy="8" r="6.5"/><ellipse class="icon" cx="8" cy="8" rx="2.8" ry="6.5"/><line class="icon" x1="1.5" y1="8" x2="14.5" y2="8"/></svg>
      </li>
    </ul>
  </section>

</body>
</html>
```